Priority Goals poster for school year

We are an elementary school and the past two years have had you help us to design a "poster" that illustrates our goal of the coming year. I am attaching our last year's one, along with some photos of our (ver rough) thinking for next years. The priority goal at top remains the same. Can't wait to see your genius ideas! :)

Target Market(s)

Staff of an elementary school and parents to some (informative) extent as well.

Colors
296eb1
6094c6
fbed22
fbee3f

Requirements
Must have
• items from the white board picture we have attached

```html
<!DOCTYPE html>
<html lang="en">
<head>
<meta charset="utf-8">
<title>2021-2022 Priority Goals Poster</title>
<link href="https://fonts.googleapis.com/css2?family=Lato:wght@400;700;900&display=swap" rel="stylesheet">
<style>
  :root{
    --blue:#296eb1;
    --blue-mid:#6094c6;
    --blue-soft:#5e8fc2;
    --paper:#dbe6f2;
    --yellow:#fbed22;
    --yellow-soft:#fbee3f;
    --ink:#1d1d1b;
    --white:#ffffff;
    --stage:#ffffff;
  }
  *{box-sizing:border-box;margin:0;padding:0}
  html,body{width:1200px;height:1200px;overflow:hidden;background:var(--stage)}
  body{position:relative;font-family:'Lato',sans-serif}
  .poster{position:absolute;left:213px;top:51px;width:774px;height:1098px;background:var(--paper);overflow:hidden}
  .school-name{position:absolute;left:26px;top:40px;width:150px;display:flex;align-items:flex-start;gap:8px;color:var(--blue);font-weight:900;font-size:17px;line-height:1.1}
  .school-name .mark{flex:none;width:16px;height:16px;background:var(--yellow);margin-top:2px}
  .year{position:absolute;right:32px;top:26px;font-weight:900;font-size:52px;color:var(--blue-mid);letter-spacing:.5px}
  .title{position:absolute;right:22px;top:74px;font-weight:900;font-size:51px;color:var(--blue);letter-spacing:.3px}
  .decor{position:absolute;left:0;top:270px;width:774px;height:680px;background:radial-gradient(ellipse at 80% 35%,rgba(255,255,255,.35),rgba(255,255,255,0) 55%),radial-gradient(ellipse at 12% 60%,rgba(255,255,255,.3),rgba(255,255,255,0) 50%)}
  .diagram{position:absolute;left:0;top:0}
  .banner-text{font-family:'Lato',sans-serif;font-size:12.5px;fill:var(--white)}
  .hex-text{font-family:'Lato',sans-serif;font-size:13px;fill:var(--white)}
  .hex-head{font-family:'Lato',sans-serif;font-size:15px;font-weight:700;fill:var(--yellow)}
  .hub-top{font-family:'Lato',sans-serif;font-size:31px;font-weight:900;fill:var(--blue)}
  .hub-bottom{font-family:'Lato',sans-serif;font-size:31px;font-weight:900;fill:var(--ink)}
  .promises{position:absolute;left:0;width:774px;top:840px;text-align:center;font-weight:900;font-size:31px;line-height:39px;color:var(--blue)}
  .footer{position:absolute;left:0;bottom:0;width:774px;height:67px;background:var(--blue);display:flex;align-items:center;justify-content:center;gap:12px;color:var(--white);font-weight:700;font-size:22px}
  .footer .mark{width:20px;height:20px;background:var(--white)}
</style>
</head>
<body>
<main class="poster">
  <div class="school-name"><span class="mark"></span><span>RIDGEVIEW ELEMENTARY SCHOOL</span></div>
  <div class="year">2021- 2022</div>
  <h1 class="title">PRIORITY GOALS</h1>

  <div class="decor" role="img" aria-label="Faint decorative music note swirls in the background"></div>

  <svg class="diagram" width="774" height="1098" viewBox="0 0 774 1098">
    <!-- banner row -->
    <g class="banner">
      <rect x="26" y="146" width="220" height="55" fill="var(--blue-mid)"/>
      <rect x="520" y="146" width="231" height="55" fill="var(--blue-mid)"/>
      <rect x="232" y="146" width="300" height="55" rx="27.5" fill="var(--blue-soft)" stroke="var(--paper)" stroke-width="5"/>
      <text class="banner-text" text-anchor="middle"><tspan x="122" y="169">Be intentional with</tspan><tspan x="122" y="185">pads action-focus</tspan></text>
      <text class="banner-text" text-anchor="middle"><tspan x="381" y="171">Staff doing what they love teaching kids</tspan><tspan x="381" y="187">for proven growth</tspan></text>
      <text class="banner-text" text-anchor="middle"><tspan x="651" y="163">Mental health for every</tspan><tspan x="651" y="179">person in our school</tspan><tspan x="651" y="194">community</tspan></text>
    </g>

    <!-- hexagons -->
    <g fill="var(--blue)">
      <polygon points="160,283 307,283 375,407 307,531 160,531 90,407"/>
      <polygon points="480,283 627,283 695,407 627,531 480,531 410,407"/>
      <polygon points="160,542 307,542 375,666 307,790 160,790 90,666"/>
      <polygon points="480,542 627,542 695,666 627,790 480,790 410,666"/>
    </g>

    <!-- hub -->
    <circle cx="382" cy="537" r="139" fill="none" stroke="rgba(170,198,228,.55)" stroke-width="48"/>
    <rect x="210" y="533" width="344" height="8" fill="rgba(220,232,245,.7)"/>
    <polygon points="298,390 467,390 553,537 467,682 298,682 210,537" fill="none" stroke="var(--yellow)" stroke-width="1.5"/>
    <g fill="var(--yellow)">
      <circle cx="298" cy="390" r="5.5"/><circle cx="467" cy="390" r="5.5"/><circle cx="553" cy="537" r="5.5"/>
      <circle cx="467" cy="682" r="5.5"/><circle cx="298" cy="682" r="5.5"/><circle cx="210" cy="537" r="5.5"/>
    </g>
    <circle cx="382" cy="537" r="99" fill="var(--yellow)"/>
    <text class="hub-top" x="382" y="531" text-anchor="middle">PRIORITY</text>
    <text class="hub-bottom" x="382" y="564" text-anchor="middle">GOALS</text>

    <!-- top-left -->
    <text class="hex-head" x="240" y="344" text-anchor="middle">Voices of all</text>
    <text class="hex-text" text-anchor="middle"><tspan x="232" y="371">Who are we?</tspan><tspan x="237" y="397">Where are you</tspan><tspan x="237" y="415">going?</tspan></text>
    <g class="icon-voice" fill="var(--yellow)" stroke="var(--yellow)">
      <circle cx="124" cy="394" r="6" stroke="none"/>
      <path d="M113 418 a11 11 0 0 1 22 0 z" stroke="none"/>
      <path d="M140 392 a6 6 0 0 1 0 10" fill="none" stroke-width="2.5"/>
      <path d="M145 387 a12 12 0 0 1 0 20" fill="none" stroke-width="2.5"/>
      <path d="M150 382 a18 18 0 0 1 0 30" fill="none" stroke-width="2.5"/>
    </g>

    <!-- top-right -->
    <text class="hex-head" x="555" y="338" text-anchor="middle">Small</text>
    <text class="hex-text" text-anchor="middle"><tspan x="559" y="368">Measured</tspan><tspan x="560" y="395">Steps towards</tspan><tspan x="563" y="422">Higher Goal</tspan></text>
    <g class="icon-cube" stroke="var(--yellow)" fill="none" stroke-width="2">
      <path d="M633 383 v42 h40"/>
      <path d="M653 386 l14 -7 14 7 v16 l-14 7 -14 -7 z" fill="var(--yellow)" stroke="none"/>
      <path d="M653 386 l14 7 14 -7 M667 393 v16" stroke="var(--blue)"/>
    </g>

    <!-- bottom-left -->
    <text class="hex-text" text-anchor="middle"><tspan x="222" y="623">Connect</tspan><tspan x="225" y="649">Celebrate</tspan><tspan x="224" y="674">Story, predictably</tspan><tspan x="224" y="700">Laugh, have fun</tspan></text>
    <text class="hex-head" x="236" y="731" text-anchor="middle">Build value partnership:</text>
    <g class="icon-network" fill="var(--yellow)" stroke="var(--yellow)" stroke-width="1.5">
      <circle cx="136" cy="667" r="8"/>
      <line x1="136" y1="667" x2="118" y2="650"/><line x1="136" y1="667" x2="154" y2="650"/>
      <line x1="136" y1="667" x2="116" y2="684"/><line x1="136" y1="667" x2="156" y2="684"/>
      <line x1="136" y1="667" x2="136" y2="645"/>
      <circle cx="118" cy="650" r="3.5"/><circle cx="154" cy="650" r="3.5"/>
      <circle cx="116" cy="684" r="3.5"/><circle cx="156" cy="684" r="3.5"/><circle cx="136" cy="645" r="3"/>
    </g>

    <!-- bottom-right -->
    <text class="hex-text" text-anchor="middle"><tspan x="557" y="630">Expectations</tspan><tspan x="557" y="658">Support</tspan><tspan x="557" y="686">For clarity</tspan></text>
    <text class="hex-head" text-anchor="middle"><tspan x="552" y="713">Communicate, communicate,</tspan><tspan x="552" y="731">communicate!</tspan></text>
    <g class="icon-chat" fill="var(--yellow)">
      <path d="M623 662 h24 v20 h-16 l-8 7 z"/>
      <path d="M637 648 h32 a4 4 0 0 1 4 4 v18 a4 4 0 0 1 -4 4 h-4 v7 l-8 -7 h-20 a4 4 0 0 1 -4 -4 v-18 a4 4 0 0 1 4 -4 z" stroke="var(--blue)" stroke-width="2"/>
      <circle cx="646" cy="661" r="2" fill="var(--blue)"/><circle cx="653" cy="661" r="2" fill="var(--blue)"/><circle cx="660" cy="661" r="2" fill="var(--blue)"/>
    </g>
  </svg>

  <h2 class="promises">FOUNDATIONAL PROMISES (4 YEARS<br>STRONG BETTER PROMISES)</h2>

  <footer class="footer"><span class="mark"></span><span>@ridgeviewleadlearner</span></footer>
</main>
</body>
</html>
```